Brenton Wealth Management Flow Charts

I need help creating three flow charts for my businesses website. We want them to be simple but look professional. This is for a Wealth Management firm. I will attach a word document that has all of the descriptions for everything so you know what icons to use. We just want the chart to have an icon, the names of each step and the corresponding numbers. I will also include some examples of charts we liked as well. Once the winner is selected, we will need help with additional graphic design elements for our website ASAP.
- Goudy Roman

```html
<!DOCTYPE html>
<html lang="en">
<head>
<meta charset="utf-8">
<title>Financial Planning – Brenton Wealth Management</title>
<link rel="stylesheet" href="https://fonts.googleapis.com/css2?family=Pathway+Gothic+One&family=Sorts+Mill+Goudy&display=swap">
<style>
  :root {
    --bg: #d7d7d7;
    --ink: #6d6e71;
    --dark: #231f20;
    --white: #ffffff;
    --magenta: #cc509c;
    --orange: #f27f37;
    --yellow: #fcd231;
    --green: #afd14f;
    --cyan: #44bfda;
    --blue: #1677bd;
  }
  html, body {
    margin: 0;
    padding: 0;
    width: 1200px;
    height: 604px;
    overflow: hidden;
    background: var(--bg);
  }
  .process-chart {
    display: block;
    width: 1200px;
    height: 604px;
  }
  .step-label {
    font-family: "Pathway Gothic One", "Oswald", sans-serif;
    font-size: 54px;
    fill: var(--ink);
  }
  .chart-title {
    font-family: "Sorts Mill Goudy", "Goudy Bookletter 1911", serif;
    font-size: 42px;
    fill: var(--dark);
  }
  .brand-name {
    font-family: "Pathway Gothic One", "Oswald", sans-serif;
    font-size: 46px;
    fill: var(--ink);
  }
  .ring-face { fill: var(--white); }
  .icon-area { opacity: 0.85; }
</style>
</head>
<body>
<svg class="process-chart" viewBox="0 0 2500 1259" xmlns="http://www.w3.org/2000/svg" aria-label="Financial planning process in six steps">

  <g class="wave">
    <path fill="var(--magenta)" d="M162 625 A210 210 0 0 1 582 625 L520 625 A148 148 0 0 0 224 625 Z"/>
    <path fill="var(--orange)"  d="M520 625 A210 210 0 0 0 940 625 L878 625 A148 148 0 0 1 582 625 Z"/>
    <path fill="var(--yellow)"  d="M878 625 A210 210 0 0 1 1298 625 L1236 625 A148 148 0 0 0 940 625 Z"/>
    <path fill="var(--green)"   d="M1236 625 A210 210 0 0 0 1656 625 L1594 625 A148 148 0 0 1 1298 625 Z"/>
    <path fill="var(--cyan)"    d="M1594 625 A210 210 0 0 1 2014 625 L1952 625 A148 148 0 0 0 1656 625 Z"/>
    <path fill="var(--blue)"    d="M1952 625 A210 210 0 0 0 2372 625 L2310 625 A148 148 0 0 1 2014 625 Z"/>
  </g>

  <g class="joints" fill="var(--white)">
    <polygon points="535,626 565,626 550,641"/>
    <polygon points="893,624 923,624 908,609"/>
    <polygon points="1251,626 1281,626 1266,641"/>
    <polygon points="1609,624 1639,624 1624,609"/>
    <polygon points="1967,626 1997,626 1982,641"/>
  </g>

  <g class="rings">
    <circle cx="372"  cy="625" r="121" fill="var(--magenta)"/><circle class="ring-face" cx="372"  cy="625" r="104"/>
    <circle cx="730"  cy="625" r="121" fill="var(--orange)"/><circle class="ring-face" cx="730"  cy="625" r="104"/>
    <circle cx="1088" cy="625" r="121" fill="var(--yellow)"/><circle class="ring-face" cx="1088" cy="625" r="104"/>
    <circle cx="1446" cy="625" r="121" fill="var(--green)"/><circle class="ring-face" cx="1446" cy="625" r="104"/>
    <circle cx="1804" cy="625" r="121" fill="var(--cyan)"/><circle class="ring-face" cx="1804" cy="625" r="104"/>
    <circle cx="2162" cy="625" r="121" fill="var(--blue)"/><circle class="ring-face" cx="2162" cy="625" r="104"/>
  </g>

  <g class="icons">
    <circle class="icon-area" cx="372"  cy="625" r="58" fill="var(--magenta)" role="img" aria-label="Goal orientation icon"/>
    <circle class="icon-area" cx="730"  cy="625" r="58" fill="var(--orange)"  role="img" aria-label="Financial review icon"/>
    <circle class="icon-area" cx="1088" cy="625" r="58" fill="var(--yellow)"  role="img" aria-label="Planning and forecasting icon"/>
    <circle class="icon-area" cx="1446" cy="625" r="58" fill="var(--green)"   role="img" aria-label="Strategic guidance icon"/>
    <circle class="icon-area" cx="1804" cy="625" r="58" fill="var(--cyan)"    role="img" aria-label="Implementation icon"/>
    <circle class="icon-area" cx="2162" cy="625" r="58" fill="var(--blue)"    role="img" aria-label="Review process icon"/>
  </g>

  <g class="labels">
    <text class="step-label" text-anchor="middle"><tspan x="727" y="380">Financial</tspan><tspan x="727" y="433">Review</tspan></text>
    <text class="step-label" text-anchor="middle"><tspan x="1446" y="380">Strategic</tspan><tspan x="1446" y="433">Guidance</tspan></text>
    <text class="step-label" text-anchor="middle"><tspan x="2160" y="380">Our Review</tspan><tspan x="2165" y="433">Process</tspan></text>
    <text class="step-label" text-anchor="middle"><tspan x="362" y="836">Goal</tspan><tspan x="362" y="889">Orientation</tspan></text>
    <text class="step-label"><tspan x="995" y="836">Planning &amp;</tspan><tspan x="995" y="889">Forecasting</tspan></text>
    <text class="step-label" text-anchor="middle"><tspan x="1814" y="889">Implementation</tspan></text>
  </g>

  <text class="chart-title" x="55" y="1212" textLength="655" lengthAdjust="spacing">FINANCIAL PLANNING</text>
  <text class="brand-name" x="2448" y="1212" text-anchor="end">Brenton Wealth Management</text>
</svg>
</body>
</html>
```